Premium Wraparound Label Design for 6 oz Mellow Spread Jar – Lanakila Sweet Kitchen

Design a continuous wraparound label for an 6 oz circular glass jar that integrates the Lanakila Sweet Kitchen logo (featuring the pink and brown leaf motif) and the Mellow Spread nutrition label into one cohesive, premium presentation. The design should feel authentically Hawaiian, classic, and handcrafted—reflecting the brand’s legacy of island-inspired desserts.
Label Specifications
Container: 8 oz round glass jar
Label Type: Full wraparound (one continuous label)
Approximate Label Size: 2.5 inches tall × 8.5 inches wide
Finish: Matte or satin with optional gold foil highlights
Print: CMYK-ready artwork with bleed and safe zones clearly marked
Design Elements to Integrate
1. Front Panel (Main Display Area):
Prominently feature the Lanakila Sweet Kitchen logo centered and scaled proportionally.
Display the product name “Mellow Spread” in elegant, legible typography that complements the logo.
Add the following text beneath or near the product name:
“Made in Hawai‘i”
“Net Wt. 8 oz (227g)”
“Keep Refrigerated” (in smaller but clear type).
Background tones should complement the logo—cream, soft tan, or pastel pink for warmth and harmony.
The front should communicate island sophistication—premium yet inviting.
2. Side Panel (Transition Area):
Create a smooth visual transition around the jar using a subtle, continuous background pattern such as tropical leaves, ocean wave textures, or gold accent lines.
Include the brand story text:
“Lanakila Sweet Kitchen brings authentic island flavors to every table. Our signature Mellow Spread blends tropical fruit and fresh cream for a taste of pure aloha.”
3. Back Panel (Informational Area):
Integrate the Mellow Spread nutrition facts panel and ingredients list (from the attached file).
Ensure layout is FDA-compliant, legible, and well-balanced.
Beneath the ingredients, include:
“Manufactured by Lanakila Sweet Kitchen, Hawai‘i.”
“Keep Refrigerated.”
Leave space for:
A QR code linking to the brand website and social media.
A barcode area, placed neatly near the bottom or corner.
Aesthetic Direction
Style: Premium, classic, and island-inspired
Color Palette: Cream base with warm browns, muted pinks, and gold accents
Typography:
Serif or script for product name and logo (for a classic, handcrafted look)
Clean sans-serif for informational text
Mood: Heritage meets handcrafted luxury — nostalgic yet refined
Finish Options:
Matte for artisanal authenticity
Satin or metallic foil for a modern, premium touch
Deliverables
Designers should submit:
3 design variations (e.g., classic heritage, minimalist modern, and premium tropical).
Editable source files (AI, PSD, or layered PDF) with bleed and safe zones clearly marked.
Mockups on an 8 oz round glass jar for visual presentation.

Target Market(s)

Craft fair consumers / tourist in hawaii

Industry/Entity Type

food and Bev

Logo Text

see description

Font styles to use
Serif
Sans Serif
Script

Requirements
Must have
• see description
Nice to have
• see description
Should not have
• see description

```html
<!DOCTYPE html>
<html lang="en">
<head>
<meta charset="utf-8">
<title>Mellow Spread – Wraparound Label Variations</title>
<link rel="stylesheet" href="https://fonts.googleapis.com/css2?family=Arimo:wght@400;700&family=Baloo+2:wght@800&family=Cormorant+Garamond:wght@600&family=Josefin+Sans:wght@400;600&family=Roboto+Condensed:wght@300;400&display=swap">
<style>
  :root{
    --brown:#532f12;
    --brown-soft:#6a3f20;
    --cream:#e8dccd;
    --cream-soft:#efe4d6;
    --pink:#d98c8f;
    --pink-light:#f7d5d6;
    --pink-deep:#e9aeb1;
    --gold-1:#b8860b;
    --gold-2:#f6e27a;
    --gold-3:#c9a227;
    --bg-light:#ececec;
    --bg-dark:#d2d2d2;
    --ink:#1d1d1d;
  }
  *{margin:0;padding:0;box-sizing:border-box}
  html,body{width:1200px;height:1200px;overflow:hidden}
  body{
    position:relative;
    background:linear-gradient(135deg,var(--bg-light) 0 50%,var(--bg-dark) 50% 100%);
    font-family:"Roboto Condensed",sans-serif;
  }
  .label{
    position:absolute;left:72px;width:1069px;height:314px;
    box-shadow:-6px 8px 10px rgba(0,0,0,.35);
    display:flex;
  }
  .label--one{top:177px}
  .label--two{top:646px}
  .label::before,.label::after{
    content:"";position:absolute;left:0;right:0;height:6px;z-index:3;
    background:linear-gradient(90deg,var(--gold-1),var(--gold-2) 30%,var(--gold-3) 55%,var(--gold-2) 80%,var(--gold-1));
  }
  .label::before{top:0}
  .label::after{bottom:0}
  .panel{position:relative;height:100%;overflow:hidden}
  .panel--back{width:374px}
  .panel--front{width:391px}
  .panel--side{width:304px}
  .tone-dark{background:var(--brown);color:var(--cream-soft)}
  .tone-light{background:var(--cream);color:var(--brown)}
  .leaf-pattern{position:absolute;inset:0;pointer-events:none}
  .tone-dark .leaf-pattern{background:radial-gradient(ellipse 60% 55% at 70% 50%,rgba(140,90,55,.35),transparent 70%)}
  .tone-light .leaf-pattern{background:radial-gradient(ellipse 60% 55% at 70% 50%,rgba(205,180,160,.35),transparent 70%)}

  .nutrition{
    position:absolute;left:31px;top:20px;width:130px;height:272px;overflow:hidden;
    border:1px solid #3a2a20;
    background:linear-gradient(135deg,var(--pink-deep),var(--pink-light) 45%,#f3b7b2 75%,var(--pink-deep));
    color:var(--ink);font-family:"Arimo",sans-serif;padding:2px 3px;
  }
  .nutrition h3{font-size:16px;font-weight:700;line-height:19px;letter-spacing:-.4px;white-space:nowrap}
  .nf-small{font-size:6.5px;line-height:9px}
  .nf-bar{height:5px;background:#222;margin:2px 0}
  .nf-cal{display:flex;justify-content:space-between;font-size:13.5px;font-weight:700;line-height:16px;border-bottom:3px solid #222;padding-bottom:1px}
  .nf-row{font-size:6px;line-height:10.4px;border-top:.6px solid #666}
  .nf-row.indent{padding-left:8px}
  .nf-right{text-align:right;font-weight:700;font-size:5.5px;line-height:9px}
  .nf-vit{font-size:5.5px;line-height:9px;border-top:2px solid #222}
  .nf-ing{font-size:6.5px;line-height:8.2px;border-top:.6px solid #666;padding-top:2px}
  b{font-weight:700}

  .maker{position:absolute;left:186px;width:180px;text-align:center;font-size:12px;line-height:15px;font-weight:400}
  .maker--credit{top:107px}
  .maker--storage{top:168px}

  .brand{position:absolute;left:0;right:0;text-align:center}
  .brand-mark{position:absolute;left:50%;top:40px;width:44px;height:44px;margin-left:-22px;border-radius:50%;background:var(--pink)}
  .brand-name{top:98px;font-family:"Cormorant Garamond",serif;font-weight:600;font-size:34px;line-height:34px;letter-spacing:2px;text-transform:uppercase}
  .tone-light .brand-name{color:var(--brown)}
  .tone-dark .brand-name{color:var(--cream)}
  .brand-est{top:193px;font-family:"Josefin Sans",sans-serif;font-weight:600;font-size:10px;letter-spacing:1px;display:flex;justify-content:center;align-items:center;gap:8px}
  .brand-est::before,.brand-est::after{content:"";width:22px;height:1px;background:currentColor}
  .product{top:212px;font-family:"Baloo 2",sans-serif;font-weight:800;font-size:42px;line-height:50px;color:var(--pink);letter-spacing:1px}
  .net{position:absolute;left:47px;bottom:14px;font-size:11px}
  .origin{position:absolute;right:40px;bottom:12px;font-size:19px}

  .story{position:absolute;left:39px;top:36px;width:236px;font-size:12px;line-height:15px}
  .qr-slot{position:absolute;left:91px;top:139px;width:127px;height:127px;background:#fff;border:2px solid var(--gold-3)}
</style>
</head>
<body>

<section class="label label--one">
  <div class="panel panel--back tone-dark">
    <div class="leaf-pattern" role="img" aria-label="Faint tropical leaf pattern"></div>
    <div class="nutrition">
      <h3>Nutrition Facts</h3>
      <div class="nf-small">Serving Size 1 serving</div>
      <div class="nf-bar"></div>
      <div class="nf-small"><b>Amount Per Serving</b></div>
      <div class="nf-cal"><span>Calories</span><span>150</span></div>
      <div class="nf-right">%Daily Value*</div>
      <div class="nf-row"><b>Total Fat</b> 13g</div>
      <div class="nf-row indent">Saturated Fat 8g</div>
      <div class="nf-row indent">Trans Fat 0g</div>
      <div class="nf-row"><b>Cholesterol</b> 55mg</div>
      <div class="nf-row"><b>Sodium</b> 5mg</div>
      <div class="nf-row"><b>Total Carbohydrate</b> 10g</div>
      <div class="nf-row indent">Dietary Fiber 0g</div>
      <div class="nf-row indent">Total Sugars 9g</div>
      <div class="nf-row indent">Includes Added Sugars 8g</div>
      <div class="nf-row"><b>Protein</b> 1g</div>
      <div class="nf-vit">• Vitamin D 10% DV • Calcium 2% DV<br>• Iron 0% DV • Potassium 1% DV</div>
      <div class="nf-ing"><b>Ingredients</b>: Guava concentrate, Unsalted butter (cream, natural flavor), Cane sugar, Whole eggs, Egg yolks, Proprietary blend of natural flavors and spices.</div>
    </div>
    <p class="maker maker--credit">Manufactured by<br>Lanakila Sweet Kitchen, Hawaiʻi.</p>
    <p class="maker maker--storage">Keep Refrigerated.</p>
  </div>
  <div class="panel panel--front tone-light">
    <div class="leaf-pattern" role="img" aria-label="Faint tropical leaf pattern"></div>
    <span class="brand-mark"></span>
    <p class="brand brand-name">Lanakila<br>Sweet Kitchen</p>
    <p class="brand brand-est">EST 1999</p>
    <h2 class="brand product">MELLOW SPREAD</h2>
    <p class="net">Net Wt. 6 oz (170g)</p>
    <p class="origin">Made in Hawaiʻi</p>
  </div>
  <div class="panel panel--side tone-dark">
    <div class="leaf-pattern" role="img" aria-label="Faint tropical leaf pattern"></div>
    <p class="story">Lanakila Sweet Kitchen brings authentic island flavors to every table. Our signature Mellow Spread blends tropical fruit and fresh cream for a taste of pure aloha.</p>
    <div class="qr-slot"></div>
  </div>
</section>

<section class="label label--two">
  <div class="panel panel--back tone-light">
    <div class="leaf-pattern" role="img" aria-label="Faint tropical leaf pattern"></div>
    <div class="nutrition">
      <h3>Nutrition Facts</h3>
      <div class="nf-small">Serving Size 1 serving</div>
      <div class="nf-bar"></div>
      <div class="nf-small"><b>Amount Per Serving</b></div>
      <div class="nf-cal"><span>Calories</span><span>150</span></div>
      <div class="nf-right">%Daily Value*</div>
      <div class="nf-row"><b>Total Fat</b> 13g</div>
      <div class="nf-row indent">Saturated Fat 8g</div>
      <div class="nf-row indent">Trans Fat 0g</div>
      <div class="nf-row"><b>Cholesterol</b> 55mg</div>
      <div class="nf-row"><b>Sodium</b> 5mg</div>
      <div class="nf-row"><b>Total Carbohydrate</b> 10g</div>
      <div class="nf-row indent">Dietary Fiber 0g</div>
      <div class="nf-row indent">Total Sugars 9g</div>
      <div class="nf-row indent">Includes Added Sugars 8g</div>
      <div class="nf-row"><b>Protein</b> 1g</div>
      <div class="nf-vit">• Vitamin D 10% DV • Calcium 2% DV<br>• Iron 0% DV • Potassium 1% DV</div>
      <div class="nf-ing"><b>Ingredients</b>: Guava concentrate, Unsalted butter (cream, natural flavor), Cane sugar, Whole eggs, Egg yolks, Proprietary blend of natural flavors and spices.</div>
    </div>
    <p class="maker maker--credit">Manufactured by<br>Lanakila Sweet Kitchen, Hawaiʻi.</p>
    <p class="maker maker--storage">Keep Refrigerated.</p>
  </div>
  <div class="panel panel--front tone-dark">
    <div class="leaf-pattern" role="img" aria-label="Faint tropical leaf pattern"></div>
    <span class="brand-mark"></span>
    <p class="brand brand-name">Lanakila<br>Sweet Kitchen</p>
    <p class="brand brand-est">EST 1999</p>
    <h2 class="brand product">MELLOW SPREAD</h2>
    <p class="net">Net Wt. 6 oz (170g)</p>
    <p class="origin">Made in Hawaiʻi</p>
  </div>
  <div class="panel panel--side tone-light">
    <div class="leaf-pattern" role="img" aria-label="Faint tropical leaf pattern"></div>
    <p class="story">Lanakila Sweet Kitchen brings authentic island flavors to every table. Our signature Mellow Spread blends tropical fruit and fresh cream for a taste of pure aloha.</p>
    <div class="qr-slot"></div>
  </div>
</section>

</body>
</html>
```